lawn sign

Lawn Sign
Roofing Gutters Windows

Target Market(s)

roofing

Font styles to use
Sans Serif

Colors
86cfc6
33a6d7
fbee3f
faa54b

Requirements
Must have
• my logo
Nice to have
• designer for now

```html
<!DOCTYPE html>
<html lang="en">
<head>
<meta charset="utf-8">
<title>Harlow Restoration – Lawn Sign</title>
<link rel="stylesheet" href="https://fonts.googleapis.com/css2?family=Cinzel:wght@400;700;800&display=swap">
<style>
  :root {
    --page-bg: #e8ebe6;
    --sign-white: #ffffff;
    --brand-teal: #1f8a7a;
    --band-blue-top: #2379b6;
    --band-blue-bottom: #173f78;
    --hex-green: #8dc63f;
    --hex-edge: #2a7bbf;
    --strip-green-left: #a2cd45;
    --strip-green-right: #58b049;
    --text-light: #ffffff;
  }
  * { margin: 0; padding: 0; box-sizing: border-box; }
  html, body {
    width: 1200px; height: 1200px; overflow: hidden;
    background: var(--page-bg);
    font-family: "Cinzel", Georgia, serif;
  }
  .lawn-sign {
    position: absolute; left: 0; top: 150px;
    width: 1200px; height: 900px;
    background: var(--sign-white);
    overflow: hidden;
  }
  .sign-shapes { position: absolute; inset: 0; }
  .brand-block {
    position: absolute; right: 150px; top: 110px;
    text-align: right; color: var(--brand-teal);
    font-weight: 400; line-height: 1.05;
  }
  .brand-name { font-size: 86px; letter-spacing: 1px; }
  .brand-line { font-size: 50px; }
  .brand-mark {
    display: inline-block; width: 22px; height: 22px;
    border-radius: 50%; background: var(--brand-teal);
    margin-right: 14px; vertical-align: middle;
  }
  .service-label {
    position: absolute; color: var(--text-light);
    font-weight: 800; font-size: 44px; letter-spacing: 1px;
    line-height: 1;
    transform: translateX(-50%); white-space: nowrap;
  }
  .call-pill {
    position: absolute; left: 120px; top: 670px;
    width: 960px; height: 100px;
    border: 2px solid var(--text-light); border-radius: 50px;
    display: flex; align-items: center; justify-content: center;
    color: var(--text-light); font-weight: 800; font-size: 60px;
  }
  .web-address {
    position: absolute; left: 0; right: 0; top: 812px;
    text-align: center; color: var(--text-light);
    font-weight: 700; font-size: 40px; letter-spacing: 30px;
    padding-left: 30px;
  }
</style>
</head>
<body>
<div class="lawn-sign">
  <svg class="sign-shapes" width="1200" height="900" viewBox="0 0 1200 900">
    <defs>
      <linearGradient id="bandBlue" x1="0" y1="0" x2="0" y2="1">
        <stop offset="0" stop-color="var(--band-blue-top)"/>
        <stop offset="1" stop-color="var(--band-blue-bottom)"/>
      </linearGradient>
      <linearGradient id="stripGreen" x1="0" y1="0" x2="1" y2="0">
        <stop offset="0" stop-color="var(--strip-green-left)"/>
        <stop offset="1" stop-color="var(--strip-green-right)"/>
      </linearGradient>
    </defs>
    <path class="service-band" d="M0 585 Q560 430 1200 440 L1200 900 L0 900 Z" fill="url(#bandBlue)"/>
    <rect class="web-strip" x="0" y="790" width="1200" height="110" fill="url(#stripGreen)"/>

    <g class="service-icon roofing" transform="translate(250 520)">
      <polygon points="0,-62 54,-31 54,31 0,62 -54,31 -54,-31" fill="var(--hex-green)" stroke="var(--hex-edge)" stroke-width="4"/>
      <path d="M-28 2 L0 -24 L28 2 M-20 -5 V26 H20 V-5 M-6 26 V10 H6 V26" fill="none" stroke="#fff" stroke-width="5" stroke-linejoin="round"/>
    </g>
    <g class="service-icon windows" transform="translate(580 465)">
      <polygon points="0,-62 54,-31 54,31 0,62 -54,31 -54,-31" fill="var(--hex-green)" stroke="var(--hex-edge)" stroke-width="4"/>
      <path d="M-28 -24 H28 V26 H-28 Z M-28 -16 H28 M0 -16 V26 M-28 18 H28" fill="none" stroke="#fff" stroke-width="5" stroke-linejoin="round"/>
    </g>
    <g class="service-icon gutters" transform="translate(910 430)">
      <polygon points="0,-62 54,-31 54,31 0,62 -54,31 -54,-31" fill="var(--hex-green)" stroke="var(--hex-edge)" stroke-width="4"/>
      <path d="M-26 -8 H26 L20 8 H-20 Z M2 8 V28 H12 M12 8 V20" fill="none" stroke="#fff" stroke-width="5" stroke-linejoin="round"/>
      <path d="M-12 -28 V-20 M0 -28 V-20 M12 -28 V-20" stroke="#fff" stroke-width="4"/>
    </g>
  </svg>

  <div class="brand-block">
    <div class="brand-name"><span class="brand-mark"></span>HARLOW</div>
    <div class="brand-line">Restoration</div>
    <div class="brand-line">Remodeling Group LLC</div>
  </div>

  <div class="service-label" style="left:250px; top:598px;">ROOFING</div>
  <div class="service-label" style="left:580px; top:543px;">WINDOWS</div>
  <div class="service-label" style="left:910px; top:508px;">GUTTERS</div>

  <div class="call-pill">CALL US: (555) 014-2870</div>
  <div class="web-address">WWW.HARLOWLLC.COM</div>
</div>
</body>
</html>
```